Wine Label Design

A wine label for 750ml bottles. Same label for different varieties with the variety / region / vintage to be updated as required.
Brand: Beyond the Ridge
Product Use: Front and Back label suitable for a 750 ml bottle (preferably Burgundy bottles)
Design Brief: Beyond the Ridge is a small winery that produces limited amounts of hand crafted wines that are aimed at the mid to top end of the market and requires a label befitting the work that goes into the creation of the wine. In terms of style i don't have any preconceptions and am open to a broad range of design suggestions at the same level of existing premium brands or innovative brands.
Must Have for Front label
Front Label
Beyond the Ridge
2013
Grampians
Shiraz
750ML (should be in smaller text)
Alc. 14% by Vol. (should be in smaller text)
Must Have for Back Label
Beyond the Ridge
2013
Grampians
Shiraz
www.beyondtheridge.com.au (should be in smaller text)
Product of Australia
Alc.14% by Vol. (should be in smaller text)
Contains preservative 220(should be in smaller text)
Below are some guides for dimensions:
The Front Label Size can be between
100 - 120 mm (Width) x 70 - 85 mm (Height)
The back label size can be between
90 mm (Width) x 70 - 85 mm (Height)
Target Market(s)
Medium to top end of the wine market who require the label to be a reflection of the wine.
Industry/Entity Type
Product
Colors
Designer to choose colors to be used in the design.
Look and feel

```html
<!DOCTYPE html>
<html lang="en">
<head>
<meta charset="utf-8">
<title>Beyond the Ridge – 2013 Grampians Shiraz Label</title>
<link rel="stylesheet" href="https://fonts.googleapis.com/css2?family=Tinos&display=swap">
<style>
  :root {
    --paper: #f2ede3;
    --paper-shade: #e9e2d4;
    --frame: #111111;
    --ink-dark: #1c1a19;
    --ink-soft: #4a4443;
    --ink-fine: #2a2726;
  }
  html, body {
    margin: 0;
    padding: 0;
    width: 1200px;
    height: 1109px;
    overflow: hidden;
    background: var(--paper);
  }
  .label {
    position: relative;
    width: 1200px;
    height: 1109px;
    background: radial-gradient(ellipse at 50% 45%, var(--paper) 55%, var(--paper-shade) 100%);
    font-family: "Tinos", "Times New Roman", serif;
    text-align: center;
  }
  .label__frame {
    position: absolute;
    inset: 14px;
    border: 6px solid var(--frame);
  }
  .brand-name {
    position: absolute;
    top: 200px;
    left: 0;
    right: 0;
    margin: 0;
    font-size: 92px;
    font-weight: 400;
    line-height: 1;
    color: var(--ink-dark);
  }
  .vintage {
    position: absolute;
    top: 438px;
    left: 0;
    right: 0;
    margin: 0;
    font-size: 86px;
    font-weight: 400;
    line-height: 1;
    color: var(--ink-soft);
  }
  .region, .variety {
    position: absolute;
    left: 0;
    right: 0;
    margin: 0;
    font-size: 44px;
    line-height: 1;
    color: var(--ink-soft);
  }
  .region { top: 566px; }
  .variety { top: 634px; }
  .details {
    position: absolute;
    top: 872px;
    left: 0;
    right: 0;
    margin: 0;
    padding: 0;
    list-style: none;
    font-size: 25px;
    line-height: 34px;
    color: var(--ink-fine);
  }
</style>
</head>
<body>
  <main class="label">
    <div class="label__frame"></div>
    <h1 class="brand-name">Beyond the Ridge</h1>
    <p class="vintage">2013</p>
    <p class="region">Grampians</p>
    <p class="variety">Shiraz</p>
    <ul class="details">
      <li>www.beyondtheridge.com.au</li>
      <li>Product of Australia</li>
      <li>750ML</li>
      <li>Alc.14% by Vol.</li>
      <li>Contains preservative 220</li>
    </ul>
  </main>
</body>
</html>
```